Blue Harbor Path

Have clients check their mortgage qualifications before they go looking for a mortgage lender. This program gains access to your lenders credit report / 3 scores without impacting your credit scores.

```html
<!DOCTYPE html>
<html lang="en">
<head>
<meta charset="utf-8">
<title>Blue Harbor Path — Business Card</title>
<link rel="stylesheet" href="https://fonts.googleapis.com/css2?family=Roboto:wght@400;500;700&display=swap">
<style>
  :root {
    --page-bg: #d6d6d6;
    --card-white: #ffffff;
    --brand-blue: #0a45c8;
    --brand-blue-deep: #0639b0;
    --brand-green: #12c46e;
    --text-grey: #3a3a3a;
    --shadow: rgba(0, 0, 0, 0.18);
  }
  * { box-sizing: border-box; margin: 0; padding: 0; }
  html, body {
    width: 1200px;
    height: 800px;
    overflow: hidden;
    background: var(--page-bg);
    font-family: "Roboto", Arial, sans-serif;
  }
  .canvas {
    position: relative;
    width: 1200px;
    height: 800px;
    display: flex;
    align-items: center;
    justify-content: center;
    gap: 60px;
  }
  .card {
    width: 500px;
    height: 286px;
    border-radius: 22px;
    box-shadow: 0 10px 28px var(--shadow);
    position: relative;
    overflow: hidden;
  }

  /* Front: contact side */
  .card-front {
    background: var(--card-white);
    display: flex;
    align-items: center;
  }
  .front-brand {
    width: 250px;
    display: flex;
    flex-direction: column;
    align-items: center;
    justify-content: center;
    gap: 14px;
  }
  .brand-square {
    width: 58px;
    height: 58px;
    border-radius: 8px;
    background: var(--brand-blue);
  }
  .brand-name {
    font-family: "Roboto", Arial, sans-serif;
    font-weight: 500;
    font-size: 26px;
    letter-spacing: 0.3px;
    color: var(--brand-blue);
    white-space: nowrap;
  }
  .divider {
    width: 1.5px;
    height: 118px;
    background: var(--brand-blue);
  }
  .contact-block {
    padding-left: 22px;
    color: var(--text-grey);
  }
  .person-name {
    font-weight: 700;
    font-size: 17px;
    color: var(--brand-blue);
    letter-spacing: 0.2px;
  }
  .person-title {
    font-weight: 500;
    font-size: 12px;
    color: var(--brand-green);
    margin-top: 1px;
  }
  .address {
    font-size: 11px;
    line-height: 1.35;
    margin-top: 10px;
  }
  .contact-list {
    list-style: none;
    margin-top: 8px;
    font-size: 11px;
    line-height: 1.4;
  }
  .contact-list li {
    display: flex;
    align-items: center;
    gap: 6px;
  }
  .contact-icon {
    width: 10px;
    height: 10px;
    flex: none;
  }

  /* Back: brand side */
  .card-back {
    background: linear-gradient(160deg, var(--brand-blue) 0%, var(--brand-blue-deep) 100%);
    display: flex;
    flex-direction: column;
    align-items: center;
    justify-content: center;
    gap: 18px;
  }
  .card-back .brand-square {
    width: 72px;
    height: 72px;
    background: var(--card-white);
  }
  .card-back .brand-name {
    color: var(--card-white);
    font-size: 32px;
  }
</style>
</head>
<body>
<main class="canvas">

  <section class="card card-front" aria-label="Business card, contact side">
    <div class="front-brand">
      <div class="brand-square" aria-hidden="true"></div>
      <div class="brand-name">Blue Harbor Path</div>
    </div>
    <div class="divider" aria-hidden="true"></div>
    <div class="contact-block">
      <p class="person-name">DANA WHITLOW</p>
      <p class="person-title">President</p>
      <p class="address">412 Cedar Hollow Road<br>Fairview, Oregon 97024</p>
      <ul class="contact-list">
        <li>
          <svg class="contact-icon" viewBox="0 0 10 10" aria-hidden="true"><path d="M2 1 L4 1 L4.6 3 L3.4 3.8 Q4.4 5.8 6.2 6.6 L7 5.4 L9 6 L9 8 Q8.5 9 7.5 9 Q1 8 1 2.5 Q1 1.5 2 1 Z" fill="var(--brand-green)"/></svg>
          555-210-4830
        </li>
        <li>
          <svg class="contact-icon" viewBox="0 0 10 10" aria-hidden="true"><rect x="2.5" y="0.5" width="5" height="9" rx="1" fill="none" stroke="var(--brand-green)" stroke-width="1.2"/></svg>
          555-318-2764
        </li>
        <li>
          <svg class="contact-icon" viewBox="0 0 10 10" aria-hidden="true"><rect x="1" y="3" width="8" height="5.5" rx="0.8" fill="var(--brand-green)"/><rect x="3" y="1" width="4" height="2.5" fill="var(--brand-green)"/></svg>
          555-427-9105
        </li>
        <li>
          <svg class="contact-icon" viewBox="0 0 10 10" aria-hidden="true"><rect x="0.5" y="2" width="9" height="6" rx="0.8" fill="var(--brand-green)"/><path d="M1 2.5 L5 5.5 L9 2.5" fill="none" stroke="#fff" stroke-width="0.9"/></svg>
          info@blueharborpath.com
        </li>
        <li>
          <svg class="contact-icon" viewBox="0 0 10 10" aria-hidden="true"><circle cx="5" cy="5" r="4.3" fill="var(--brand-green)"/><path d="M0.7 5 H9.3 M5 0.7 Q2.5 5 5 9.3 M5 0.7 Q7.5 5 5 9.3" fill="none" stroke="#fff" stroke-width="0.7"/></svg>
          blueharborpath.com
        </li>
      </ul>
    </div>
  </section>

  <section class="card card-back" aria-label="Business card, brand side">
    <div class="brand-square" aria-hidden="true"></div>
    <div class="brand-name">Blue Harbor Path</div>
  </section>

</main>
</body>
</html>
```